Product Brochure Design - Front and Back Cover
DRFTW Company Product Brochure Design
We have uploaded a new image to the project, we like how people are using the contrast of black into the image so could use this new image to emphasis our products. more images to come.....
Please also note the we DO NOT want the complete solutions provider tag on the brochure.....
Kindly brand nook have reopened this contest for a further 5 days due to issues at our end. I will be eliminating some designs and adding some direction for the designs we like.
Apologies for not mentioning before but this is an A4 portrait book. There will be print bleed margins of 3mm.

```html
<!DOCTYPE html>
<html lang="en">
<head>
<meta charset="utf-8">
<title>DRFTW Construction Supplies – Brochure Covers</title>
<link href="https://fonts.googleapis.com/css2?family=Arimo:wght@400;700&display=swap" rel="stylesheet">
<style>
  :root {
    --ink: #0d0d0d;
    --paper: #ffffff;
    --accent: #f5c400;
    --brand-orange: #f39a1e;
    --sky: #6fa4d8;
    --foliage: #4f6b34;
    --stone: #d9cfbe;
    --steel: #9aa3a8;
  }
  * { margin: 0; padding: 0; box-sizing: border-box; }
  html, body { width: 1200px; height: 847px; overflow: hidden; background: var(--paper); }
  body { font-family: "Arimo", Arial, sans-serif; color: var(--ink); }

  .spread { position: relative; width: 1200px; height: 847px; display: flex; }
  .page { position: relative; width: 600px; height: 847px; overflow: hidden; }

  /* Back cover */
  .back-photo {
    position: absolute; left: 0; top: 0; width: 600px; height: 516px;
    background: linear-gradient(180deg, var(--sky) 0%, #a9c8e6 35%, var(--foliage) 62%, #3a5128 100%);
  }
  .back-band {
    position: absolute; left: 0; top: 516px; width: 600px; height: 175px;
    background: var(--ink);
    display: flex; align-items: center; justify-content: center;
  }
  .back-contact {
    position: absolute; left: 34px; top: 703px;
    font-size: 11px; line-height: 14px; color: var(--ink); font-style: normal;
  }
  .back-strip {
    position: absolute; left: 0; bottom: 0; width: 600px; height: 38px;
    background: var(--accent);
  }

  /* Brand name block */
  .brand { display: flex; align-items: center; gap: 14px; }
  .brand-square { width: 34px; height: 34px; background: var(--brand-orange); }
  .brand-name { font-weight: 700; line-height: 1; text-align: left; }
  .brand-name .word { display: block; font-size: 44px; letter-spacing: 2px; }
  .brand-name .sub { display: block; font-size: 17px; letter-spacing: 1px; margin-top: 4px; }
  .brand--light .brand-name { color: var(--paper); }
  .brand--dark .brand-name { color: var(--ink); }

  /* Front cover */
  .front-head {
    position: absolute; left: 0; top: 0; width: 600px; height: 211px;
    background: var(--paper);
    display: flex; align-items: center; justify-content: center;
  }
  .front-photo {
    position: absolute; left: 0; top: 211px; width: 600px; height: 475px;
    background: linear-gradient(160deg, #c9bca6 0%, var(--stone) 40%, var(--steel) 75%, #7d878c 100%);
  }
  .front-band {
    position: absolute; left: 0; top: 686px; width: 600px; height: 161px;
    background: var(--ink);
    display: flex; align-items: center; justify-content: center;
  }
  .front-web {
    font-size: 13px; color: var(--accent); font-weight: 700;
  }
</style>
</head>
<body>
<main class="spread">
  <section class="page page--back">
    <div class="back-photo" role="img" aria-label="Photograph of a suspension bridge with scaffolded tower above a wooded gorge"></div>
    <div class="back-band">
      <div class="brand brand--light">
        <span class="brand-square"></span>
        <span class="brand-name"><span class="word">DRFTW</span><span class="sub">CONSTRUCTION SUPPLIES</span></span>
      </div>
    </div>
    <address class="back-contact">
      The Harbour Lantern Company Limited<br>
      Unit F, Kestrel Distribution Centre, Millward Way,<br>
      Eastport, Bramford, BF11 9QT<br>
      Tel: +44 (0) 1632 96 01 50 – Fax: +44 (0) 1632 96 01 51<br>
      Email: office@harbourlantern.co.uk<br>
      www.harbourlantern.co.uk
    </address>
    <div class="back-strip"></div>
  </section>

  <section class="page page--front">
    <header class="front-head">
      <div class="brand brand--dark">
        <span class="brand-square"></span>
        <span class="brand-name"><span class="word">DRFTW</span><span class="sub">CONSTRUCTION SUPPLIES</span></span>
      </div>
    </header>
    <div class="front-photo" role="img" aria-label="Photograph of a worker in safety harness climbing steel scaffolding against a stone building"></div>
    <footer class="front-band">
      <p class="front-web">www.harbourlantern.co.uk</p>
    </footer>
  </section>
</main>
</body>
</html>
```